Single Page/Scrolling Design for Model Recruitment site

We need a design (and if you are capable, coding) for our company, Vero Parlour Room (LA as in Los Angeles). We like modern single page designs, hence the title for the project. We have already had a designer come up with a logo, which is attached. You're free to play around with the colors, although we want the site to have a feminine appeal to it.

The site is basically a recruitment project for girls who are interested in working as chat hosts for cam sites. We don't want anything cheesy that feels like a porn site. The inspiration for the logo (and the inspiration for the site) comes from the French and English salons of the late 18th century, where beautiful and intelligent women would gather to discuss a range of topics. We want the website to convey that this work is fun and exciting. Please keep these things in mind for the design.

As I mentioned, we like the modern look and feel of single page designs, especially because we don't have a ton of content. We just need an "About us" area, a "Work from Home" area, a "Work at The Parlour Room" area, and "Contact Us" area which should have text boxes for entering email, subject, a message, etc.

The logo I mentioned is attached, as well as a very crude mockup of the layout of all the content I described.

Target Market(s)

Women age 18-35.

Industry/Entity Type

It Company

Font styles to use
Serif
Decorative
Script

Colors

Designer to choose colors to be used in the design.

Requirements
Should not have
• Images that are super sexual or even slightly pornographic. We want this to appeal to a broad range of women.

```html
<!DOCTYPE html>
<html lang="en">
<head>
<meta charset="utf-8">
<title>Vero Parlour Room — Webcam Modeling</title>
<link href="https://fonts.googleapis.com/css2?family=Raleway:wght@200;300;400;800&display=swap" rel="stylesheet">
<style>
  :root {
    --pink: #e4137f;
    --header-bg: #2c2c2c;
    --hero-bg-dark: #3a3a3a;
    --hero-bg-light: #8a8a8a;
    --white: #ffffff;
    --text-grey: #8a8a8a;
    --text-dark: #222222;
    --nav-grey: #9a9a9a;
    --strip: #f2f2f2;
  }
  * { margin: 0; padding: 0; box-sizing: border-box; }
  html, body { width: 1072px; height: 1200px; overflow: hidden; background: var(--white); }
  body { position: relative; font-family: 'Raleway', sans-serif; }

  .site-header { position: absolute; left: 0; top: 0; width: 1072px; height: 75px; background: var(--header-bg); }
  .brand { position: absolute; left: 72px; top: 26px; display: flex; align-items: center; gap: 8px;
    color: var(--pink); font-size: 14px; font-weight: 400; }
  .brand-dot { width: 18px; height: 18px; border-radius: 50%; background: var(--pink); }
  .main-nav { position: absolute; right: 92px; top: 32px; display: flex; gap: 26px; }
  .main-nav a { color: var(--nav-grey); font-size: 11px; letter-spacing: 2.6px; text-decoration: none; text-transform: uppercase; }
  .main-nav a.is-active { color: var(--pink); }

  .hero { position: absolute; left: 0; top: 75px; width: 1072px; height: 455px; overflow: hidden; }
  .hero-photo { position: absolute; inset: 0;
    background: linear-gradient(100deg, var(--hero-bg-dark) 0%, #5e5a58 35%, var(--hero-bg-light) 70%, #6e6e6e 100%); }
  .hero-brand { position: absolute; left: 0; width: 100%; top: 88px; display: flex; justify-content: center; align-items: center; gap: 10px;
    color: var(--pink); font-size: 20px; font-weight: 400; }
  .hero-brand .brand-dot { width: 24px; height: 24px; }
  .hero-title { position: absolute; left: 0; width: 100%; top: 163px; text-align: center; color: var(--white);
    font-size: 80px; line-height: 1; letter-spacing: -1px; white-space: nowrap; }
  .hero-title .thin { font-weight: 200; }
  .hero-title .bold { font-weight: 800; }
  .hero-sub { position: absolute; top: 250px; left: 0; width: 100%; text-align: center; color: var(--pink); font-size: 17px; font-weight: 300; }
  .hero-rule { position: absolute; top: 259px; height: 1px; background: var(--white); width: 184px; }
  .hero-rule.left { left: 166px; } .hero-rule.right { left: 718px; }
  .hero-btn { position: absolute; left: 464px; top: 297px; width: 140px; height: 47px; border: 1px solid var(--white);
    color: var(--white); font-size: 15px; font-weight: 300; display: flex; align-items: center; justify-content: center; }
  .hero-arrow { position: absolute; top: 187px; }
  .hero-arrow.prev { left: 10px; } .hero-arrow.next { left: 988px; }
  .hero-scroll { position: absolute; left: 509px; top: 365px; }

  .about-title { position: absolute; top: 598px; left: 0; width: 100%; text-align: center; font-size: 35px; font-weight: 300; color: var(--text-dark); }
  .about-divider { position: absolute; top: 648px; left: 500px; }
  .about-lead { position: absolute; top: 672px; left: 266px; width: 540px; text-align: center; color: var(--text-grey);
    font-size: 15.5px; line-height: 22px; font-weight: 400; }
  .about-body { position: absolute; left: 89px; top: 799px; width: 420px; color: var(--text-grey); font-size: 13.5px; line-height: 28px; font-weight: 300; }
  .about-body p + p { margin-top: 25px; }
  .about-body em { font-style: normal; color: var(--pink); }
  .about-btn { position: absolute; left: 89px; top: 1034px; width: 183px; height: 51px; border: 1px solid var(--text-dark);
    color: var(--text-dark); font-size: 15px; display: flex; align-items: center; justify-content: center; }
  .about-photo { position: absolute; left: 593px; top: 790px; width: 416px; height: 304px;
    background: linear-gradient(90deg, #c9d3b8 0%, #eef0ec 35%, #c8a58a 65%, #d9ddd0 100%); }
  .footer-strip { position: absolute; left: 0; top: 1195px; width: 1072px; height: 5px; background: var(--strip); }
</style>
</head>
<body>
  <header class="site-header">
    <div class="brand"><span class="brand-dot"></span>Vero Parlour Room</div>
    <nav class="main-nav">
      <a class="is-active" href="#home">Home</a>
      <a href="#about">About</a>
      <a href="#train">Train @ The Parlour Room</a>
      <a href="#work">Work From Home</a>
      <a href="#contact">Contact</a>
    </nav>
  </header>

  <section class="hero" id="home">
    <div class="hero-photo" role="img" aria-label="Woman sitting on the floor working at a laptop"></div>
    <div class="hero-brand"><span class="brand-dot"></span>Vero Parlour Room</div>
    <h1 class="hero-title"><span class="thin">WEBCAM </span><span class="bold">MODELING</span></h1>
    <span class="hero-rule left"></span>
    <p class="hero-sub">WELCOME TO THE VERO PARLOUR ROOM</p>
    <span class="hero-rule right"></span>
    <a class="hero-btn">START NOW!</a>
    <svg class="hero-arrow prev" width="68" height="68" viewBox="0 0 68 68"><circle cx="34" cy="34" r="32" fill="none" stroke="#fff" stroke-width="2"/><path d="M40 26 L28 34 L40 42 Z" fill="#fff"/></svg>
    <svg class="hero-arrow next" width="68" height="68" viewBox="0 0 68 68"><circle cx="34" cy="34" r="32" fill="none" stroke="#fff" stroke-width="2"/><path d="M29 26 L41 34 L29 42 Z" fill="#fff"/></svg>
    <svg class="hero-scroll" width="48" height="48" viewBox="0 0 48 48"><circle cx="24" cy="24" r="24" fill="#2e2e2e" opacity="0.8"/><path d="M19 22 L24 27 L29 22" fill="none" stroke="#fff" stroke-width="2.2"/></svg>
  </section>

  <section id="about">
    <h2 class="about-title">ABOUT US</h2>
    <svg class="about-divider" width="72" height="12" viewBox="0 0 72 12">
      <g fill="none" stroke="#e4137f" stroke-width="1.2">
        <path d="M6 1 L11 6 L6 11 L1 6 Z"/><path d="M27 1 L32 6 L27 11 L22 6 Z"/><path d="M48 1 L53 6 L48 11 L43 6 Z"/><path d="M69 1 L71.5 6 L69 11 L64 6 Z" transform="translate(-2 0)"/>
      </g>
    </svg>
    <p class="about-lead">The Vero Parlour Room was started with the understanding that there is a large number of women sho are curious about working in webcam intertainment but have no idea where to start.</p>
    <div class="about-body">
      <p>There are hundreds of <em>"studios" or "agencies"</em> on the internet with the goal of making money just by getting you to sign up, or even worse, by <em>taking a percentage of your comissions</em> once you do.</p>
      <p>That is not what <em>The Parlour Room</em> is about. We want to be the premier destination for webcam entertainers to further their careers, <em>no matter</em> what level of experiece you have.</p>
    </div>
    <a class="about-btn">START NOW!</a>
    <div class="about-photo" role="img" aria-label="Woman outdoors leaning towards an open laptop"></div>
  </section>
  <div class="footer-strip"></div>
</body>
</html>
```